Directing people to check over 2000 new Portugal listings on the site

A copy of our failed attempt is annexed. graphics should be 197x650px and 448x81px

Target Market(s)

Global property Buyers

Requirements
Nice to have
• Euro map with portugal isolated

```html
<!DOCTYPE html>
<html lang="en">
<head>
<meta charset="utf-8">
<title>2000 New Listings in the Mediterranean – Banners</title>
<link rel="stylesheet" href="https://fonts.googleapis.com/css2?family=Open+Sans:wght@400;700&family=Roboto+Condensed:wght@700&display=swap">
<style>
  :root {
    --stage: #4a3424;
    --red: #d0171d;
    --red-dark: #8c0e12;
    --yellow: #ffe100;
    --green: #2e9e3a;
    --navy: #24308a;
    --sky: #1fa6e2;
    --sea: #8fd0ee;
    --sea-deep: #5fb8e4;
    --land: #86c06a;
    --land-light: #b9d99a;
    --sand: #f3e4c6;
    --ink: #3a3a3a;
    --white: #ffffff;
  }
  * { margin: 0; padding: 0; box-sizing: border-box; }
  html, body { width: 1200px; height: 1200px; overflow: hidden; }
  body { background: var(--stage); position: relative; font-family: "Open Sans", sans-serif; }

  .size-label { position: absolute; color: var(--white); font-family: "Open Sans", sans-serif; font-weight: 400; font-size: 30px; }
  .size-label--skyscraper { left: 163px; top: 36px; }
  .size-label--leaderboard { left: 993px; top: 474px; }

  .banner { position: absolute; overflow: hidden; box-shadow: 6px 8px 14px rgba(0,0,0,.55); }
  .banner svg { position: absolute; inset: 0; }

  .skyscraper { left: 94px; top: 118px; width: 298px; height: 982px; }
  .skyscraper__lead {
    position: absolute; left: 14px; width: 270px; top: 526px;
    text-align: center; color: var(--ink); font-weight: 700; font-size: 25px; line-height: 33px;
  }
  .skyscraper__headline {
    position: absolute; left: 0; width: 298px; top: 722px; text-align: center;
    font-family: "Roboto Condensed", sans-serif; font-weight: 700; text-shadow: 2px 2px 3px rgba(0,0,0,.45);
  }
  .headline__accent { color: var(--yellow); font-size: 54px; line-height: 60px; display: block; }
  .headline__sub { color: var(--white); font-size: 36px; line-height: 44px; display: block; }
  .skyscraper__headline .headline__sub:first-of-type { margin-top: 10px; }

  .leaderboard { left: 461px; top: 550px; width: 677px; height: 122px; }
  .leaderboard__lead {
    position: absolute; left: 84px; width: 132px; top: 9px; text-align: center;
    color: var(--white); font-weight: 700; font-size: 13.5px; line-height: 17.5px;
  }
  .leaderboard__headline {
    position: absolute; left: 232px; width: 440px; top: 10px; text-align: center;
    font-family: "Roboto Condensed", sans-serif; font-weight: 700; text-shadow: 2px 2px 3px rgba(0,0,0,.45);
  }
  .leaderboard__headline .headline__accent { font-size: 46px; line-height: 52px; }
  .leaderboard__headline .headline__sub { font-size: 40px; line-height: 46px; }
</style>
</head>
<body>
  <div class="size-label size-label--skyscraper">197x650</div>
  <div class="size-label size-label--leaderboard">448x81</div>

  <section class="banner skyscraper">
    <svg width="298" height="982" viewBox="0 0 298 982">
      <defs>
        <linearGradient id="redFill" x1="0" y1="0" x2="1" y2="1">
          <stop offset="0" stop-color="var(--red)"/>
          <stop offset="1" stop-color="var(--red-dark)"/>
        </linearGradient>
        <linearGradient id="mapFill" x1="0" y1="0" x2="0" y2="1">
          <stop offset="0" stop-color="var(--sea-deep)"/>
          <stop offset=".18" stop-color="var(--sea)"/>
          <stop offset=".32" stop-color="var(--land)"/>
          <stop offset=".52" stop-color="var(--land-light)"/>
          <stop offset=".62" stop-color="var(--sea)"/>
          <stop offset=".72" stop-color="var(--sand)"/>
          <stop offset="1" stop-color="var(--sand)"/>
        </linearGradient>
        <clipPath id="discClip"><circle cx="150" cy="345" r="362"/></clipPath>
        <clipPath id="stripeCorners">
          <rect x="0" y="0" width="120" height="130"/>
          <rect x="190" y="560" width="108" height="200"/>
        </clipPath>
      </defs>
      <rect width="298" height="982" fill="url(#redFill)"/>
      <g clip-path="url(#stripeCorners)">
        <circle cx="150" cy="345" r="390" fill="none" stroke="var(--yellow)" stroke-width="10"/>
        <circle cx="150" cy="345" r="380" fill="none" stroke="var(--green)" stroke-width="10"/>
      </g>
      <circle cx="150" cy="345" r="368" fill="var(--sand)" stroke="var(--navy)" stroke-width="14"/>
      <g clip-path="url(#discClip)">
        <rect x="-250" y="-30" width="800" height="560" fill="url(#mapFill)" role="img" aria-label="Map of Europe and North Africa with Portugal circled"/>
        <rect x="-250" y="500" width="800" height="300" fill="var(--sand)"/>
      </g>
    </svg>
    <p class="skyscraper__lead">Check over 2000<br>new Portugal<br>listings<br>on the site</p>
    <h1 class="skyscraper__headline">
      <span class="headline__accent">2000 NEW</span>
      <span class="headline__accent">LISTINGS</span>
      <span class="headline__sub">IN THE</span>
      <span class="headline__sub">MEDITERRANEAN</span>
    </h1>
  </section>

  <section class="banner leaderboard">
    <svg width="677" height="122" viewBox="0 0 677 122">
      <defs>
        <linearGradient id="redWide" x1="0" y1="0" x2="1" y2="1">
          <stop offset="0" stop-color="var(--red)"/>
          <stop offset="1" stop-color="var(--red-dark)"/>
        </linearGradient>
        <linearGradient id="mapWide" x1="0" y1="0" x2="0" y2="1">
          <stop offset="0" stop-color="var(--sea)"/>
          <stop offset=".4" stop-color="var(--land)"/>
          <stop offset=".7" stop-color="var(--land-light)"/>
          <stop offset="1" stop-color="var(--sand)"/>
        </linearGradient>
        <linearGradient id="skyFade" x1="0" y1="0" x2="1" y2="0">
          <stop offset="0" stop-color="var(--sky)" stop-opacity="0"/>
          <stop offset=".3" stop-color="var(--sky)"/>
          <stop offset="1" stop-color="var(--sky)"/>
        </linearGradient>
      </defs>
      <rect width="240" height="122" fill="url(#mapWide)" role="img" aria-label="Map of Europe and North Africa with Portugal circled"/>
      <path d="M60,0 L222,0 Q200,61 222,122 L60,122 Q90,61 60,0Z" fill="url(#skyFade)"/>
      <path d="M214,0 Q190,61 214,122" fill="none" stroke="var(--yellow)" stroke-width="5"/>
      <path d="M220,0 Q196,61 220,122" fill="none" stroke="var(--green)" stroke-width="5"/>
      <path d="M226,0 Q202,61 226,122" fill="none" stroke="var(--navy)" stroke-width="6"/>
      <path d="M229,0 L677,0 L677,122 L229,122 Q205,61 229,0Z" fill="url(#redWide)"/>
    </svg>
    <p class="leaderboard__lead">Check<br>Over 2000<br>New Portugal<br>Listings<br>On The Site</p>
    <h2 class="leaderboard__headline">
      <span class="headline__accent">2000 NEW LISTINGS</span>
      <span class="headline__sub">IN THE MEDITERRANEAN</span>
    </h2>
  </section>
</body>
</html>
```